Need a business card design for a residential architect.

You can get a sense of his work at www.tbrolvik.com

Would like a consistent look and feel between business card and website
.

Target Market(s)

Residential homeowners builders

Industry/Entity Type

Residential

Contact Information for Business Card

Dale Brolvik
Principle
Brolvik Architecture
418 Quill Lane
Menlo Park, CA 94025

dale@tbrolvik.com

tbrolvik.com
phone: 650-555-0172
Fax: 650-555-0196

Font styles to use
Sans Serif

Requirements
Must have
• Details above
Nice to have
• Would like a consistent look and feel between business card and website
Should not have
• None

```html
<!DOCTYPE html>
<html lang="en">
<head>
<meta charset="utf-8">
<title>Brolvik Architecture — Business Card</title>
<link rel="stylesheet" href="https://fonts.googleapis.com/css2?family=Open+Sans:wght@400;600;700&display=swap">
<style>
  :root {
    --backdrop: #3a302b;
    --card: #8a8a8a;
    --ink: #ffffff;
    --ink-soft: #f2f2f2;
    --rule: rgba(255, 255, 255, 0.85);
  }
  * { box-sizing: border-box; margin: 0; padding: 0; }
  html, body {
    width: 1200px;
    height: 780px;
    overflow: hidden;
    background: var(--backdrop);
    font-family: "Open Sans", sans-serif;
    color: var(--ink);
  }
  .stage {
    position: relative;
    width: 1200px;
    height: 780px;
  }
  .card {
    position: absolute;
    top: 235px;
    width: 540px;
    height: 310px;
    background: var(--card);
    border-radius: 3px;
    box-shadow: 0 10px 24px rgba(0, 0, 0, 0.35);
  }
  .card--front { left: 40px; }
  .card--back { left: 620px; }

  .wordmark {
    position: absolute;
    font-weight: 600;
    color: var(--ink);
    line-height: 1;
  }
  .wordmark__name {
    display: block;
    letter-spacing: 0.02em;
  }
  .wordmark__trade {
    display: block;
    letter-spacing: 0.62em;
  }
  .card--front .wordmark { left: 60px; top: 70px; }
  .card--front .wordmark__name { font-size: 82px; }
  .card--front .wordmark__trade { font-size: 20px; margin-top: 6px; }

  .card--back .wordmark { left: 165px; top: 36px; }
  .card--back .wordmark__name { font-size: 64px; }
  .card--back .wordmark__trade { font-size: 16px; margin-top: 4px; }

  .holder {
    position: absolute;
    left: 30px;
    top: 150px;
    width: 210px;
    text-align: right;
  }
  .holder__name {
    font-weight: 700;
    font-size: 21px;
    margin-bottom: 8px;
    text-align: left;
  }
  .holder__line {
    font-size: 13px;
    line-height: 1.55;
    color: var(--ink-soft);
  }
  .divider {
    position: absolute;
    left: 255px;
    top: 190px;
    width: 1px;
    height: 92px;
    background: var(--rule);
  }
  .contact {
    position: absolute;
    left: 272px;
    top: 190px;
    list-style: none;
  }
  .contact__item {
    display: flex;
    align-items: center;
    gap: 8px;
    font-size: 14px;
    line-height: 23px;
    color: var(--ink-soft);
  }
  .contact__icon {
    width: 12px;
    height: 12px;
    flex: none;
    fill: var(--ink);
  }
</style>
</head>
<body>
<main class="stage">
  <section class="card card--front" aria-label="Card front">
    <div class="wordmark">
      <span class="wordmark__name">BROLVIK</span>
      <span class="wordmark__trade">ARCHITECTURE</span>
    </div>
  </section>

  <section class="card card--back" aria-label="Card back">
    <div class="wordmark">
      <span class="wordmark__name">BROLVIK</span>
      <span class="wordmark__trade">ARCHITECTURE</span>
    </div>

    <div class="holder">
      <p class="holder__name">Dale Brolvik</p>
      <p class="holder__line">Principle</p>
      <p class="holder__line">418 Quill Lane</p>
      <p class="holder__line">Menlo Park, CA 94025</p>
    </div>

    <div class="divider"></div>

    <ul class="contact">
      <li class="contact__item">
        <svg class="contact__icon" viewBox="0 0 24 24" aria-hidden="true"><path d="M6.6 10.8a15.1 15.1 0 0 0 6.6 6.6l2.2-2.2c.3-.3.7-.4 1-.2 1.1.4 2.3.6 3.6.6.6 0 1 .4 1 1V20c0 .6-.4 1-1 1A17 17 0 0 1 3 4c0-.6.4-1 1-1h3.5c.6 0 1 .4 1 1 0 1.3.2 2.5.6 3.6.1.3 0 .7-.2 1z"/></svg>
        650.555.0172
      </li>
      <li class="contact__item">
        <svg class="contact__icon" viewBox="0 0 24 24" aria-hidden="true"><path d="M7 2h8l3 3v4H7zM4 10h16a2 2 0 0 1 2 2v8a2 2 0 0 1-2 2H4a2 2 0 0 1-2-2v-8a2 2 0 0 1 2-2zm2 4v2h4v-2zm8 0v2h2v-2zm0 3v2h2v-2z"/></svg>
        650-555-0196
      </li>
      <li class="contact__item">
        <svg class="contact__icon" viewBox="0 0 24 24" aria-hidden="true"><path d="M2 5h20v14H2zm2 2v.5l8 5 8-5V7zm0 2.8V17h16V9.8l-8 5z"/></svg>
        dale@tbrolvik.com
      </li>
      <li class="contact__item">
        <svg class="contact__icon" viewBox="0 0 24 24" aria-hidden="true"><path d="M12 2a10 10 0 1 0 0 20 10 10 0 0 0 0-20zm6.9 6h-3a15 15 0 0 0-1.3-3.8A8 8 0 0 1 18.9 8zM12 4c.8 1.2 1.5 2.5 1.9 4h-3.8c.4-1.5 1.1-2.8 1.9-4zM4.3 14a8 8 0 0 1 0-4h3.4a16 16 0 0 0 0 4zm.8 2h3a15 15 0 0 0 1.3 3.8A8 8 0 0 1 5.1 16zm3-8h-3a8 8 0 0 1 4.3-3.8A15 15 0 0 0 8.1 8zM12 20c-.8-1.2-1.5-2.5-1.9-4h3.8c-.4 1.5-1.1 2.8-1.9 4zm2.3-6H9.7a14 14 0 0 1 0-4h4.6a14 14 0 0 1 0 4zm.3 5.8a15 15 0 0 0 1.3-3.8h3a8 8 0 0 1-4.3 3.8zm1.7-5.8a16 16 0 0 0 0-4h3.4a8 8 0 0 1 0 4z"/></svg>
        www.tbrolvik.com
      </li>
    </ul>
  </section>
</main>
</body>
</html>
```